Corvane Collective Web Presence Design and Relaunch

Take existing web files and "clean up" for a a more presentable web landing pad.
posted presently on a site pad CSS template. at www.corvanecollective.org

The site is clunky and unprofessional looking. Needs to be toned down so the urgency is conveyed, but not via a burning planet image.

Target Market(s)

Non-profit climate adaptation group targeting local government land management agencies, special districts and private landholders of natural resource properties.

Industry/Entity Type

Environment

Coding

Coded - Design and coding required

Number of Pages Required

4 page

Font styles to use
Serif
Sans Serif

Requirements
Must have
• Include current logos, aspects if content on current site www.corvanecollective.org
• A regional Pacific Northwest Focus (US & Canada). Content speaking to urgency but respectful of cultural diversity and norms. Sustainability themes. Emphasis on action and implementation.
Nice to have
• link to like minded projects. Appear to future generations. Diversity in thematic areas ecological resiliency, energy, food security and infrastructure.

```html
<!DOCTYPE html>
<html lang="en">
<head>
<meta charset="utf-8">
<title>Corvane Collective</title>
<link href="https://fonts.googleapis.com/css2?family=Cinzel:wght@400;600&family=Montserrat:wght@400;500;600;700&display=swap" rel="stylesheet">
<style>
:root{
  --navy:#0b3152;
  --topbar:#0f5c8c;
  --blue:#1a6ea6;
  --teal:#2f7b9a;
  --green:#8cc63f;
  --green-dark:#76a936;
  --grey:#8a8a8a;
  --text:#333;
  --white:#fff;
}
*{box-sizing:border-box;margin:0;padding:0}
html,body{width:1200px;height:2989px;overflow:hidden;background:#fff}
body{font-family:"Montserrat",sans-serif;color:var(--text);position:relative}
.abs{position:absolute}
.serif{font-family:"Cinzel",serif}

.topbar{top:0;left:0;width:1200px;height:30px;background:var(--topbar);color:#fff;font-size:14px}
.topbar .item{top:7px;display:flex;align-items:center;gap:8px}
.header{top:30px;left:0;width:1200px;height:103px;background:var(--navy)}
.brand{left:86px;top:36px;display:flex;align-items:center;gap:10px;color:var(--green);font-weight:700;font-size:20px}
.brand .dot{width:28px;height:28px;border-radius:50%;background:var(--green)}
.nav{top:62px;display:flex;gap:0;font-family:"Cinzel",serif;font-size:17px;color:#fff}
.nav a{position:absolute;color:#fff;text-decoration:none;white-space:nowrap}
.nav a.active{color:var(--green)}
.nav a.active::after{content:"";position:absolute;left:0;right:0;bottom:-14px;height:2px;background:var(--green)}
.donate{left:960px;top:53px;width:154px;height:34px;border:2px solid var(--green);border-radius:18px;color:var(--green);font-family:"Cinzel",serif;font-weight:600;font-size:17px;display:flex;align-items:center;justify-content:center}

.hero{top:133px;left:0;width:1200px;height:436px}
.hero .left{left:0;top:0;width:594px;height:436px;background:linear-gradient(180deg,#5c8fd0 0%,#9bb9dc 40%,#3f6a25 70%,#2e4d1a 100%)}
.hero .right{left:594px;top:0;width:606px;height:436px;background:linear-gradient(180deg,#6a4a2a 0%,#c07a2e 35%,#8a5a2a 65%,#6b5540 100%)}
.hero h1{font-family:"Montserrat",sans-serif;font-weight:700;color:#fff;font-size:44px;text-shadow:0 2px 6px rgba(0,0,0,.6);white-space:nowrap}
.hero h2{font-weight:700;color:#fff;font-size:32px;text-shadow:0 2px 6px rgba(0,0,0,.6);white-space:nowrap}
.dots{top:395px;left:563px;display:flex;gap:8px}
.dots span{width:12px;height:12px;border:2px solid #fff;background:#fff}
.dots span.on{background:var(--green)}

.center{left:0;width:1200px;text-align:center}
.welcome-title{top:605px;font-family:"Cinzel",serif;font-size:27px;color:#222;letter-spacing:1px}
.rule{height:3px;background:var(--green);width:86px;left:557px}
.welcome-sub{top:678px;font-size:22px;color:var(--blue)}
.welcome-text{top:720px;left:180px;width:840px;font-size:14px;line-height:26.5px;text-align:center;color:#222}

.card{top:826px;width:235px;text-align:center}
.card .ph{width:235px;height:128px}
.card h3{margin-top:20px;font-size:13.5px;font-weight:600;color:#222}
.card p{margin-top:8px;font-size:13px;line-height:21px;color:#333;padding:0 6px;height:66px}
.card .btn{display:inline-block;margin-top:10px;width:118px;height:26px;line-height:26px;border-radius:14px;background:var(--green-dark);color:#fff;font-size:13px}
.card .btn.blue{background:var(--blue)}

.band{top:1164px;left:0;width:1200px;height:200px;background:linear-gradient(90deg,#2b3f1a 0%,#44602a 45%,#2a3a18 100%)}
.band h2{left:84px;top:40px;font-family:"Cinzel",serif;font-size:29px;color:#fff;letter-spacing:1px}
.band p{left:85px;top:89px;width:800px;font-size:14px;line-height:26.5px;color:#fff;font-weight:500}
.band .art{left:900px;top:12px;width:200px;height:178px;background:radial-gradient(circle,rgba(140,198,63,.35),rgba(140,198,63,0) 70%)}

.works-title{top:1424px;font-size:21px;font-weight:700;color:#222;letter-spacing:.5px}
.work{top:1504px;width:235px}
.work .ph{width:235px;height:190px}
.work .label{height:46px;line-height:46px;text-align:center;color:#fff;font-weight:600;font-size:13.5px;background:var(--grey);margin-top:3px}
.work .sub{height:25px;line-height:25px;text-align:center;color:#fff;font-size:13px;background:#7a7a7a;border-top:1px solid rgba(255,255,255,.4)}
.work.on .label,.work.on .sub{background:var(--green-dark)}
.arrow{top:1620px}

.facts{top:1842px;left:0;width:1200px;height:467px}
.facts .img{left:0;top:0;width:504px;height:467px;background:radial-gradient(ellipse at 50% 55%,#3a2a1e 0%,#2a2018 45%,#3a4a2a 100%)}
.facts .panel{left:504px;top:0;width:696px;height:467px;background:var(--teal)}
.facts h2{left:28px;top:42px;font-family:"Cinzel",serif;font-size:23px;color:#fff;letter-spacing:.5px}
.facts .line{left:28px;top:95px;width:160px;height:3px;background:var(--green)}
.facts p{left:28px;top:116px;width:582px;font-size:14px;line-height:23px;color:#fff;text-align:justify}
.stat{display:flex;align-items:center;gap:20px;color:#fff}
.stat b{display:block;font-size:32px;font-weight:600}
.stat span{font-size:14px;color:#a8e06a}
.vline{width:1px;background:rgba(255,255,255,.3)}
.hline{height:1px;background:rgba(255,255,255,.3)}

.skills-img{left:86px;top:2366px;width:486px;height:235px;background:linear-gradient(135deg,#4f7d2a,#2e2a20 55%,#6a8a3a)}
.skills-tag{left:86px;top:2576px;width:379px;height:50px;background:#222;color:#fff;font-family:"Cinzel",serif;font-size:24px;display:flex;align-items:center;justify-content:center}
.skills-tag em{font-style:normal;color:var(--green)}
.bar-label{left:642px;font-size:13px;font-weight:600;color:#222}
.bar{left:642px;width:412px;height:8px;background:#ccc}
.bar i{display:block;height:8px;background:var(--green)}
.pct{left:1068px;width:42px;height:18px;border-radius:9px;background:#555;color:#fff;font-size:12px;font-weight:600;text-align:center;line-height:18px}

.footer{top:2688px;left:0;width:1200px;height:272px;background:var(--navy);color:#fff}
.footer h4{font-family:"Cinzel",serif;font-size:17px;font-weight:400;top:52px}
.footer .fl{top:90px;width:44px;height:2px;background:var(--green)}
.footer .fcol{top:116px;font-size:14px;line-height:26.5px}
.footer .fdiv{top:60px;width:1px;height:160px;background:rgba(255,255,255,.15)}
.social{top:117px;left:982px;display:flex;gap:8px}
.social span{width:27px;height:27px;border-radius:50%;background:var(--green)}
.copy{top:2960px;left:0;width:1200px;height:29px;background:var(--topbar);color:#fff;font-size:13px;text-align:center;line-height:29px}
</style>
</head>
<body>

<div class="abs topbar">
  <div class="abs item" style="left:802px">
    <svg width="13" height="13" viewBox="0 0 24 24"><path fill="#8cc63f" d="M6.6 10.8a15 15 0 0 0 6.6 6.6l2.2-2.2a1 1 0 0 1 1-.25 11.4 11.4 0 0 0 3.6.57 1 1 0 0 1 1 1V20a1 1 0 0 1-1 1A17 17 0 0 1 3 4a1 1 0 0 1 1-1h3.5a1 1 0 0 1 1 1c0 1.25.2 2.45.57 3.57a1 1 0 0 1-.25 1z"/></svg>
    360-555-0148
  </div>
  <div class="abs item" style="left:938px">
    <svg width="14" height="12" viewBox="0 0 24 20"><rect x="1" y="2" width="22" height="16" rx="2" fill="#8cc63f"/><path d="M2 3l10 8 10-8" stroke="#0f5c8c" stroke-width="2" fill="none"/></svg>
    info@corvanecollective.org
  </div>
</div>

<header class="abs header">
  <div class="abs brand"><span class="dot"></span>Corvane Collective</div>
  <nav class="abs nav">
    <a class="active" style="left:458px">Home</a>
    <a style="left:562px">About Us</a>
    <a style="left:695px">Events</a>
    <a style="left:808px">Contact Us</a>
  </nav>
  <div class="abs donate">Donate Now</div>
</header>

<section class="abs hero">
  <div class="abs left" role="img" aria-label="Healthy green tree under a blue sky"></div>
  <div class="abs right" role="img" aria-label="Dry tree under a hazy orange sky"></div>
  <h1 class="abs" style="left:408px;top:168px">Climate</h1>
  <h1 class="abs" style="left:609px;top:168px">Adaptation</h1>
  <h2 class="abs" style="left:347px;top:227px">Implementing</h2>
  <h2 class="abs" style="left:610px;top:227px">Climate Strategies</h2>
  <div class="abs dots"><span class="on"></span><span></span><span></span><span></span></div>
</section>

<h2 class="abs center welcome-title">Welcome to Corvane Collective</h2>
<div class="abs rule" style="top:656px"></div>
<p class="abs center welcome-sub">Climate Adaptation - Implementing Climate Strategies</p>
<p class="abs welcome-text">Dedicated to taking action the Corvane Collective was created to help bring adaption strategies to life. Working with local communities we are committed to implementing strategies that will sustain communities throughout the Pacific Northwest for generations to come.</p>

<div class="abs card" style="left:89px">
  <div class="ph" role="img" aria-label="Glass globe resting on green grass" style="background:linear-gradient(135deg,#d8e8a0,#7fae3a)"></div>
  <h3>ADAPTATION PLANS</h3>
  <p>Communities throughout the region have adopted plans to address our changing climate.</p>
  <span class="btn blue">Learn More</span>
</div>
<div class="abs card" style="left:352px">
  <div class="ph" role="img" aria-label="Lily pads floating on water" style="background:linear-gradient(135deg,#3fae3a,#1e5a2e 50%,#6ac04a)"></div>
  <h3>ECOLOGICAL RESILIENCE</h3>
  <p>To endure change Communities need to keep their watersheds functioning.</p>
  <span class="btn">Learn More</span>
</div>
<div class="abs card" style="left:613px">
  <div class="ph" role="img" aria-label="Wind turbines over a yellow field under storm clouds" style="background:linear-gradient(180deg,#4a5a6a,#8a9aaa 60%,#d8d030 82%,#a8b020)"></div>
  <h3>ENERGY AND FOOD</h3>
  <p>Security of community food and energy have, and always will be, an essential component..</p>
  <span class="btn">Learn More</span>
</div>
<div class="abs card" style="left:874px">
  <div class="ph" role="img" aria-label="Ocean waves crashing near a cliff" style="background:linear-gradient(180deg,#3a4a5a,#a8a090 40%,#2a5a7a 70%,#1a3a4a)"></div>
  <h3>ON THE GROUND</h3>
  <p>The Alliance is familiar and growing throughout the region. Presently our work ..</p>
  <span class="btn">Learn More</span>
</div>

<section class="abs band" role="img" aria-label="Dark green leaves background">
  <h2 class="abs">WHAT WE ARE DOING ?</h2>
  <p class="abs">Dedicated to taking action the Corvane Collective was created to help bring adaption strategies to life. Working with local communities we are committed to implementing strategies that will sustain communities throughout the Pacific Northwest for generations to come.</p>
  <div class="abs art" role="img" aria-label="Glowing sprout held in cupped hands"></div>
</section>

<h2 class="abs center works-title">RECENT WORKS</h2>
<div class="abs rule" style="top:1465px"></div>

<svg class="abs arrow" style="left:26px" width="22" height="36" viewBox="0 0 22 36"><path d="M18 3L4 18l14 15" stroke="#888" stroke-width="3" fill="none"/></svg>
<svg class="abs arrow" style="left:1136px" width="22" height="36" viewBox="0 0 22 36"><path d="M4 3l14 15L4 33" stroke="#888" stroke-width="3" fill="none"/></svg>

<div class="abs work on" style="left:89px">
  <div class="ph" role="img" aria-label="Solar panels and a wind turbine in snow" style="background:linear-gradient(180deg,#5a7aa8,#c8d4e4 45%,#2a3448 70%,#e8eef4)"></div>
  <div class="label">ENERGY SAVING</div><div class="sub">Investing in clean energy</div>
</div>
<div class="abs work" style="left:352px">
  <div class="ph" role="img" aria-label="Greenhouse with rows of leafy crops" style="background:linear-gradient(180deg,#d8dcdc,#9aa8a0 40%,#4a8a2a 65%,#2a5a1a)"></div>
  <div class="label">FOOD SECURITY</div><div class="sub">Retooling agriculture</div>
</div>
<div class="abs work" style="left:613px">
  <div class="ph" role="img" aria-label="Mountain lake at sunset" style="background:linear-gradient(180deg,#5a6a4a,#8a7a5a 40%,#c87a4a 65%,#2a2a20)"></div>
  <div class="label">ECOLOGICAL RESILIENCE</div><div class="sub">Environmental Progress</div>
</div>
<div class="abs work" style="left:874px">
  <div class="ph" role="img" aria-label="Railway track through a forest at sunset" style="background:linear-gradient(180deg,#c8781a,#8a4a1a 50%,#3a2a1a)"></div>
  <div class="label">INFRASTRUCTURE</div><div class="sub">Developing rural areas</div>
</div>

<section class="abs facts">
  <div class="abs img" role="img" aria-label="Cupped hands holding dark soil"></div>
  <div class="abs panel">
    <h2 class="abs">IMPORTANT FACTS ABOUT US</h2>
    <div class="abs line"></div>
    <p class="abs">Dedicated to taking action the Corvane Collective was created to help bring adaption strategies to life. Working with local communities we are committed to implementing strategies that will sustain communities throughout the Pacific Northwest for generations to come.</p>

    <div class="abs stat" style="left:68px;top:232px">
      <svg width="56" height="56" viewBox="0 0 56 56" fill="none" stroke="#fff" stroke-width="2"><rect x="8" y="8" width="18" height="18" rx="3"/><rect x="30" y="8" width="18" height="18" rx="3"/><rect x="8" y="30" width="18" height="18" rx="3"/><rect x="30" y="30" width="18" height="18" rx="3"/></svg>
      <div><b>250 +</b><span>Projects</span></div>
    </div>
    <div class="abs stat" style="left:325px;top:232px">
      <svg width="56" height="56" viewBox="0 0 56 56" fill="none" stroke="#fff" stroke-width="2"><circle cx="32" cy="20" r="10"/><path d="M4 40h14l10 6 22-10"/><path d="M4 30h10l10 4"/></svg>
      <div><b>300 +</b><span>Donations</span></div>
    </div>
    <div class="abs stat" style="left:68px;top:346px">
      <svg width="56" height="56" viewBox="0 0 56 56" fill="none" stroke="#fff" stroke-width="2"><path d="M8 50V26l20-14 20 14v24z"/><rect x="22" y="34" width="12" height="16"/></svg>
      <div><b>17 +</b><span>Communities</span></div>
    </div>
    <div class="abs stat" style="left:325px;top:346px">
      <svg width="56" height="56" viewBox="0 0 56 56" fill="none" stroke="#fff" stroke-width="2"><circle cx="18" cy="16" r="7"/><circle cx="38" cy="16" r="7"/><path d="M6 46c0-12 6-18 12-18s12 6 12 18M26 46c0-12 6-18 12-18s12 6 12 18"/></svg>
      <div><b>70 +</b><span>Volunteers</span></div>
    </div>
    <div class="abs vline" style="left:284px;top:222px;height:95px"></div>
    <div class="abs vline" style="left:284px;top:343px;height:95px"></div>
    <div class="abs hline" style="left:130px;top:325px;width:100px"></div>
    <div class="abs hline" style="left:340px;top:325px;width:100px"></div>
  </div>
</section>

<div class="abs skills-img" role="img" aria-label="Hands holding seedlings in soil"></div>
<div class="abs skills-tag">Think&nbsp;<em>Green</em>&nbsp;! Save Money</div>

<div class="abs bar-label" style="top:2382px">CLEAN WATER</div>
<div class="abs bar" style="top:2407px"><i style="width:93%"></i></div>
<div class="abs pct" style="top:2402px">98%</div>
<div class="abs bar-label" style="top:2435px">FOREST RESCUE</div>
<div class="abs bar" style="top:2460px"><i style="width:55%"></i></div>
<div class="abs pct" style="top:2455px">56%</div>
<div class="abs bar-label" style="top:2488px">AGRICULTURE</div>
<div class="abs bar" style="top:2513px"><i style="width:83%"></i></div>
<div class="abs pct" style="top:2508px">77%</div>
<div class="abs bar-label" style="top:2541px">ALTERNATIVE ENERGY</div>
<div class="abs bar" style="top:2566px"><i style="width:86%"></i></div>
<div class="abs pct" style="top:2561px">84%</div>

<footer class="abs footer">
  <h4 class="abs" style="left:86px">Climate Adaptation</h4>
  <div class="abs fl" style="left:86px"></div>
  <p class="abs fcol" style="left:86px;width:250px;line-height:21px;top:118px">Dedicated to taking action the Corvane Collective was created to help bring adaption strategies to life.</p>
  <div class="abs fdiv" style="left:361px"></div>

  <h4 class="abs" style="left:419px">Quick Links</h4>
  <div class="abs fl" style="left:419px"></div>
  <div class="abs fcol" style="left:419px">Home<br>About Us<br>Events<br>Contact Us</div>
  <div class="abs fdiv" style="left:599px"></div>

  <h4 class="abs" style="left:679px">Contact</h4>
  <div class="abs fl" style="left:679px"></div>
  <div class="abs fcol" style="left:679px;padding-left:22px">360-555-0148<br>info@corvanecollective.org<br>218 Alder Ridge Rd,<br>Larchmont WA 98290</div>
  <svg class="abs" style="left:680px;top:123px" width="12" height="12" viewBox="0 0 24 24"><path fill="#8cc63f" d="M6.6 10.8a15 15 0 0 0 6.6 6.6l2.2-2.2a1 1 0 0 1 1-.25 11.4 11.4 0 0 0 3.6.57 1 1 0 0 1 1 1V20a1 1 0 0 1-1 1A17 17 0 0 1 3 4a1 1 0 0 1 1-1h3.5a1 1 0 0 1 1 1c0 1.25.2 2.45.57 3.57a1 1 0 0 1-.25 1z"/></svg>
  <svg class="abs" style="left:680px;top:150px" width="13" height="11" viewBox="0 0 24 20"><rect x="1" y="2" width="22" height="16" rx="2" fill="#8cc63f"/><path d="M2 3l10 8 10-8" stroke="#0b3152" stroke-width="2" fill="none"/></svg>
  <svg class="abs" style="left:681px;top:175px" width="11" height="15" viewBox="0 0 16 22"><path fill="#8cc63f" d="M8 0a8 8 0 0 0-8 8c0 6 8 14 8 14s8-8 8-14a8 8 0 0 0-8-8zm0 11a3 3 0 1 1 0-6 3 3 0 0 1 0 6z"/></svg>
  <div class="abs fdiv" style="left:932px"></div>

  <h4 class="abs" style="left:982px">Follow Us</h4>
  <div class="abs fl" style="left:982px"></div>
  <div class="abs social"><span></span><span></span><span></span><span></span></div>
</footer>
<div class="abs copy">Copyright © Corvane Collective 2020. All rights reserved.</div>

</body>
</html>
```